Kalmoret Windham & Associates

We would like a simple, professional business card using a similar font to our logo.

Industry/Entity Type

Law Firm

Contact Information for Business Card

Martin Kalmoret, Esq. 47 Tillman Lane, 2nd Floor Harlow Bay, MA 02059 Office: 781.555.0143 Cell: 508.555.0196 Email: marty@kwfirmma.com kalmoretwindhamlaw.com

Font styles to use
Other font styles liked:
• We would like to use the fonts used in the logo or similar

Colors
0054AA
0677BA
7BADD7
CADEEF
E8F1F8

Requirements
Must have
• We would like the fonts to match the logo
Nice to have
• not too much design- very simple and professional business card. I added a picture of a business card that I tried to start but I am not a designer! Hopefully it will help with the address and phone numbers and kind of what we are looking for.

```html
<!DOCTYPE html>
<html lang="en">
<head>
<meta charset="utf-8">
<title>Kalmoret Windham &amp; Associates — Business Card</title>
<link rel="stylesheet" href="https://fonts.googleapis.com/css2?family=Libre+Baskerville:wght@400;700&display=swap">
<style>
  :root {
    --navy: #1b3370;
    --paper: #ffffff;
    --ink-grey: #5a5a5a;
    --rule-grey: #8a8a8a;
    --backdrop: #d9d9d9;
  }
  * { box-sizing: border-box; margin: 0; padding: 0; }
  html, body {
    width: 1200px; height: 846px; overflow: hidden;
    background: var(--backdrop);
    font-family: "Libre Baskerville", Georgia, serif;
  }
  .stage {
    width: 1200px; height: 846px;
    display: flex; align-items: center; justify-content: center; gap: 40px;
  }
  .card {
    width: 540px; height: 309px; position: relative;
    box-shadow: 0 6px 18px rgba(0,0,0,0.12);
  }

  /* Front */
  .card--front { background: var(--paper); color: var(--navy); }
  .front-firm {
    position: absolute; left: 44px; top: 92px; width: 200px;
    display: flex; align-items: flex-start; gap: 12px;
  }
  .firm-square { width: 18px; height: 18px; background: var(--navy); flex: none; margin-top: 4px; }
  .front-firm .firm-name {
    font-size: 22px; line-height: 1.25; color: var(--navy); font-weight: 400;
  }
  .contact {
    position: absolute; left: 262px; top: 62px;
  }
  .contact .person {
    font-weight: 700; font-size: 17px; letter-spacing: 0.5px;
    text-transform: uppercase; margin-bottom: 12px; color: var(--navy);
  }
  .contact ul { list-style: none; }
  .contact li {
    display: flex; align-items: center; gap: 9px;
    font-size: 12px; color: var(--ink-grey); line-height: 22px;
  }
  .contact svg { width: 13px; height: 13px; flex: none; }
  .divider {
    position: absolute; left: 44px; right: 44px; top: 232px;
    border-top: 1px solid var(--rule-grey);
  }
  .address {
    position: absolute; left: 44px; top: 246px;
    font-size: 12.5px; color: var(--ink-grey); white-space: nowrap;
  }

  /* Back */
  .card--back {
    background: var(--navy); color: var(--paper);
    display: flex; align-items: center; justify-content: center; gap: 26px;
  }
  .back-square { width: 130px; height: 100px; background: var(--paper); flex: none; }
  .back-rule { width: 1px; height: 150px; background: var(--paper); flex: none; }
  .back-firm {
    font-size: 22px; line-height: 1.15; text-transform: uppercase;
    letter-spacing: 1px; font-weight: 400; color: var(--paper);
  }
</style>
</head>
<body>
<main class="stage">

  <section class="card card--front" aria-label="Card front">
    <div class="front-firm">
      <span class="firm-square"></span>
      <span class="firm-name">Kalmoret Windham &amp; Associates</span>
    </div>

    <div class="contact">
      <p class="person">Martin Kalmoret</p>
      <ul>
        <li>
          <svg viewBox="0 0 16 16" aria-hidden="true"><path fill="#555" d="M4 1l2.5 3-1.4 1.6c.8 2 2.3 3.5 4.3 4.3L11 8.5l3 2.5-1.3 2.6C7.4 13.3 2.7 8.6 2.4 3.3z"/></svg>
          office: 781-555-0143
        </li>
        <li>
          <svg viewBox="0 0 16 16" aria-hidden="true"><rect x="4.5" y="1" width="7" height="14" rx="1.2" fill="none" stroke="#555" stroke-width="1.2"/><line x1="7" y1="12.8" x2="9" y2="12.8" stroke="#555"/></svg>
          cell: 508-555-0196
        </li>
        <li>
          <svg viewBox="0 0 16 16" aria-hidden="true"><rect x="1" y="3" width="14" height="10" fill="#555"/><path d="M1 3l7 6 7-6" fill="none" stroke="#fff" stroke-width="1"/></svg>
          marty@kwfirmma.com
        </li>
        <li>
          <svg viewBox="0 0 16 16" aria-hidden="true"><g fill="none" stroke="#555" stroke-width="1.1"><circle cx="8" cy="8" r="6.5"/><ellipse cx="8" cy="8" rx="3" ry="6.5"/><line x1="1.5" y1="8" x2="14.5" y2="8"/></g></svg>
          kalmoretwindhamlaw.com
        </li>
      </ul>
    </div>

    <div class="divider"></div>
    <p class="address">Esq. 47 Tillman Lane, 2nd Floor Harlow Bay, MA 02059</p>
  </section>

  <section class="card card--back" aria-label="Card back">
    <div class="back-square"></div>
    <div class="back-rule"></div>
    <p class="back-firm">Kalmoret<br>Windham<br>&amp; Associates</p>
  </section>

</main>
</body>
</html>
```